BRISK Chamber Of Commerce Flyer

We need to create a 2 page PDF flyer (front and back) that uses the text in the WORD document attached, but also incorporates the logo and a few screen shots.

Goal of the 2 pager is to send out via email as well as hand out to our target audience to solicit interest

Target Market(s)

Executives At U.S. based Chambers of Commerce

Industry/Entity Type

Chamber Of Commerce

Font styles to use
Sans Serif

Colors

Designer to choose colors to be used in the design.

Requirements
Must have
• Logo
• Attractive design
• Incorporate text from WORD doc
• Include 1-2 screen shots (not these will be provided shortly...powerpoint document has some examples of what these screen shots look like, or you can visit http://www.briskvlt.example
• Also needs to have our contact information
• Dale Hutton
• CEO, Fernwick
• 555-304-8216
• dhutton@fernwick.example
• www.briskvlt.example

```html
<!DOCTYPE html>
<html lang="en">
<head>
<meta charset="utf-8">
<title>BRISK Chamber of Commerce Flyer</title>
<link rel="stylesheet" href="https://fonts.googleapis.com/css2?family=Arimo:wght@400;700&display=swap">
<style>
:root{
  --bg:#efefef;
  --paper:#ffffff;
  --blue:#1a72c4;
  --navy:#132038;
  --ink:#222222;
  --muted:#555;
  --rule:#d6d6d6;
  --photo-a:#3d6f9e;
  --photo-b:#c9d6e2;
  --photo-dark-a:#1b2b48;
  --photo-dark-b:#2f4f7c;
}
*{box-sizing:border-box;margin:0;padding:0}
html,body{width:1200px;height:1000px;overflow:hidden}
body{background:var(--bg);font-family:"Arimo",Arial,sans-serif;color:var(--ink);position:relative}
.page{position:absolute;top:150px;width:550px;height:712px;background:var(--paper);overflow:hidden}
.page--front{left:35px}
.page--back{left:615px}
.abs{position:absolute}

/* Front */
.brand{left:18px;top:18px;font-weight:700;font-size:46px;letter-spacing:2px;color:var(--navy);display:flex;align-items:center;gap:10px}
.brand .sq{width:14px;height:14px;background:var(--blue)}
.brand sup{font-size:10px;font-weight:400;letter-spacing:0;align-self:flex-start;margin-top:6px}
.url-band{left:302px;top:0;width:248px;height:78px;background:var(--blue);color:#fff;font-size:17px;font-weight:700;letter-spacing:.5px;display:flex;align-items:center;justify-content:center}
.hero-photo{left:0;top:78px;width:550px;height:169px;background:linear-gradient(100deg,var(--photo-b),#8fa9c2 45%,var(--photo-a))}
.hero-tint{left:302px;top:78px;width:248px;height:169px;background:rgba(26,90,170,.55)}
.stat-box{left:305px;top:247px;width:223px;height:100px;background:var(--navy);color:#fff;font-size:11px;line-height:1.22;padding:10px 12px}
.intro{left:22px;top:256px;width:272px;font-size:11px;line-height:1.3;color:var(--ink);text-align:justify}
.section-title{color:var(--blue);font-weight:700;font-size:18px}
.problem-title{left:22px;top:352px}
.problem-list{left:22px;top:378px;width:500px;list-style:none}
.problem-list li{display:flex;align-items:center;gap:14px;border-bottom:1px solid var(--rule);font-size:11px;line-height:1.35;padding:6px 0}
.problem-list li:last-child{border-bottom:none}
.problem-list svg{flex:0 0 28px}
.meet-title{left:28px;top:588px;font-size:18px}
.meet-title b{color:var(--navy)}
.meet-text{left:28px;top:612px;width:255px;font-size:12.3px;line-height:1.32;color:var(--navy);text-align:justify}
.front-band{left:305px;top:645px;width:245px;height:55px;background:var(--blue)}
.footer-band{left:0;top:700px;width:550px;height:12px;background:var(--navy)}

/* UI panels */
.ui{background:#fff;border:1px solid #c8d0da;box-shadow:0 2px 6px rgba(0,0,0,.25)}
.ui-rail{position:absolute;left:0;top:0;bottom:0;width:12px;background:var(--navy)}
.ui-title{font-size:10px;font-weight:700;color:var(--navy)}
.ui-card{position:absolute;border:1px solid #b9a7d8;border-radius:2px;background:#fff}
.ui-num{font-size:11px;font-weight:700;color:var(--navy)}
.ui-bar{height:3px;background:#e0e0e0;margin-top:3px;position:relative}
.ui-bar i{position:absolute;left:0;top:0;bottom:0;background:var(--blue)}
.ui-row{height:5px;border-bottom:1px solid #e3e7ec}

/* Back */
.back-panel{left:360px;top:0;width:190px;height:347px;background:var(--blue)}
.back-title{left:17px;top:12px;width:270px;font-size:19px;line-height:1.2;color:var(--blue);font-weight:700}
.steps{left:25px;top:72px;width:268px;list-style:none;font-size:11px;line-height:1.25}
.steps li{display:flex;gap:10px;margin-bottom:4px}
.steps li span{color:var(--blue);font-weight:700;flex:0 0 8px}
.levels{left:25px;top:298px;width:268px;font-size:11px;line-height:1.25;text-align:justify}
.back-photo{left:0;top:347px;width:550px;height:168px;background:linear-gradient(110deg,var(--photo-dark-a),var(--photo-dark-b) 50%,#4a6d96)}
.iterative{left:20px;top:522px;width:330px;font-size:10.6px;line-height:1.25;text-align:justify}
.clients-title{left:20px;top:606px}
.clients{left:20px;top:632px;width:330px;display:flex;flex-wrap:wrap;gap:7px 11px;font-size:8px;font-weight:700;color:var(--navy)}
.contact{left:360px;top:515px;width:190px;height:197px;background:var(--blue);color:#fff;padding:12px 14px;text-align:right}
.contact h2{font-size:17px;font-weight:700;margin-bottom:10px}
.contact p{font-size:11px;line-height:1.25;display:flex;justify-content:flex-end;align-items:center;gap:6px;margin-bottom:7px}
.contact svg{flex:0 0 12px}
.back-brand{left:376px;top:648px;font-size:34px;font-weight:700;color:var(--navy);letter-spacing:2px;display:flex;align-items:center;gap:8px}
.back-brand .sq{width:10px;height:10px;background:#fff}
</style>
</head>
<body>

<section class="page page--front">
  <div class="abs brand"><span class="sq"></span>BRISK<sup>TM</sup></div>
  <div class="abs url-band">www.briskvlt.example</div>
  <div class="abs hero-photo" role="img" aria-label="Photo of a business person working on a laptop in a bright office"></div>
  <div class="abs hero-tint"></div>
  <p class="abs intro">We know the adage “it’s cheaper to keep a client then acquire a new one”, but most Chambers spend far more time and money on prospecting new customer versus retaining current customers, when a mere 3-5% increase in retention can have a significant impact on net income.</p>
  <div class="abs stat-box">The <b>2018 NACX Operations</b> Survey reports average member retention is ~85%, with first year average member retention at ~70%. Some Chambers report first year retention as low as 40%.</div>

  <h2 class="abs section-title problem-title">THE PROBLEM</h2>
  <ul class="abs problem-list">
    <li><svg width="28" height="30" viewBox="0 0 28 30"><path d="M9 2h10v12h6L14 27 3 14h6z" fill="var(--blue)"/><text x="14" y="15" font-size="9" fill="#fff" text-anchor="middle" font-family="Arimo,sans-serif" font-weight="700">$</text></svg><span>With limited resources and budget, most Chambers spend their time on their larger members or the ones that make the most noise, ignoring the rest.</span></li>
    <li><svg width="28" height="30" viewBox="0 0 28 30"><circle cx="14" cy="9" r="6" fill="var(--blue)"/><path d="M3 28c0-8 5-12 11-12s11 4 11 12z" fill="var(--blue)"/></svg><span>Many Chambers don’t know they are losing a member, until it’s too late to keep them.</span></li>
    <li><svg width="28" height="30" viewBox="0 0 28 30"><rect x="4" y="2" width="17" height="24" rx="2" fill="none" stroke="var(--blue)" stroke-width="2"/><path d="M8 8h9M8 12h9M8 16h5" stroke="var(--blue)" stroke-width="1.6"/><circle cx="20" cy="22" r="6" fill="var(--blue)"/><text x="20" y="25.5" font-size="9" fill="#fff" text-anchor="middle" font-family="Arimo,sans-serif" font-weight="700">?</text></svg><span>Even if CRM software is used, feedback entered into these systems is self-reported by Chamber team members, often resulting in biased and inconsistently entered data.</span></li>
    <li><svg width="28" height="30" viewBox="0 0 28 30"><path d="M6 9a10 10 0 1 1-2 8" fill="none" stroke="var(--blue)" stroke-width="2"/><path d="M2 6l4 4 4-4" fill="none" stroke="var(--blue)" stroke-width="2"/><path d="M15 9v7l5 3" fill="none" stroke="var(--blue)" stroke-width="2"/></svg><span>While market research surveys can be used, they are often not consistently deployed, only provide results at the summary level (not member by member), and can be time consuming and expensive.</span></li>
  </ul>

  <h2 class="abs section-title meet-title">Meet <b>BRISK™</b></h2>
  <p class="abs meet-text">The industry’s first Retention Automation platform that assess member sentiment, improves your ability to retain members, increases recurring revenue, and maximizes member lifetime value.</p>

  <div class="abs front-band"></div>
  <div class="abs ui" style="left:318px;top:554px;width:112px;height:90px">
    <div class="abs ui-title" style="left:6px;top:5px;font-size:6px">Campaign</div>
    <div class="ui-card" style="left:6px;top:16px;width:30px;height:34px"></div>
    <div class="ui-card" style="left:40px;top:16px;width:30px;height:34px"></div>
    <div class="ui-card" style="left:74px;top:16px;width:30px;height:34px"></div>
    <div class="abs" style="left:6px;top:58px;width:98px"><div class="ui-row"></div><div class="ui-row"></div><div class="ui-row"></div><div class="ui-row"></div></div>
  </div>
  <div class="abs ui" style="left:396px;top:608px;width:96px;height:90px">
    <div class="abs ui-title" style="left:6px;top:5px;font-size:6px">Averages</div>
    <svg class="abs" style="left:6px;top:30px" width="84" height="52" viewBox="0 0 84 52"><g fill="#7d4fb8"><rect x="4" y="14" width="5" height="26"/><rect x="16" y="6" width="5" height="34"/><rect x="28" y="20" width="5" height="20"/><rect x="40" y="10" width="5" height="30"/><rect x="52" y="24" width="5" height="16"/><rect x="64" y="16" width="5" height="24"/></g><g fill="#e48a3c"><rect x="10" y="40" width="4" height="8"/><rect x="34" y="40" width="4" height="10"/><rect x="58" y="40" width="4" height="6"/></g><line x1="0" y1="40" x2="84" y2="40" stroke="#999" stroke-width=".5"/></svg>
  </div>
  <div class="abs footer-band"></div>
</section>

<section class="page page--back">
  <div class="abs back-panel"></div>
  <h2 class="abs back-title">BRISK™ helps you systematically:</h2>
  <ol class="abs steps">
    <li><span>1</span>Determine what is most important to members;</li>
    <li><span>2</span>Measure performance against importance / expectation;</li>
    <li><span>3</span>Provide real time alerts on under performance against member expectations;</li>
    <li><span>4</span>Identify key playbook actions to improve member sentiment and retain members;</li>
    <li><span>5</span>Track trends over time with benchmarking against peers;</li>
    <li><span>6</span>Integrate additional Chamber data, fueling predictive analytics and continuous learning; and</li>
    <li><span>7</span>Synchronize with existing Sales/Marketing Automation Platforms.</li>
  </ol>
  <p class="abs levels">BRISK allows you to view results on multiple levels, starting at the individual level and rolls up to the member company level and segment level.</p>

  <div class="abs ui" style="left:303px;top:22px;width:235px;height:163px">
    <div class="ui-rail"></div>
    <div class="abs ui-title" style="left:20px;top:8px">Home</div>
    <div class="abs" style="left:20px;top:26px;font-size:6px;color:var(--blue)">All &nbsp; Active &nbsp; Draft &nbsp; Closed</div>
    <div class="abs ui-title" style="left:20px;top:40px;font-size:7px">Campaign for Information</div>
    <div class="ui-card" style="left:20px;top:54px;width:64px;height:100px;padding:4px"><div style="font-size:6px">Wave 2</div><div class="ui-num">42 &nbsp; 6.6</div><div class="ui-bar"><i style="width:70%"></i></div><div class="ui-bar"><i style="width:50%"></i></div><div class="ui-bar"><i style="width:60%"></i></div></div>
    <div class="ui-card" style="left:91px;top:54px;width:64px;height:100px;padding:4px"><div style="font-size:6px">Wave 3</div><div class="ui-num">28 &nbsp; 4.8</div><div class="ui-bar"><i style="width:40%"></i></div><div class="ui-bar"><i style="width:65%"></i></div><div class="ui-bar"><i style="width:30%"></i></div></div>
    <div class="ui-card" style="left:162px;top:54px;width:64px;height:100px;padding:4px"><div style="font-size:6px">Wave 1</div><div class="ui-num">33 &nbsp; 5.2</div><div class="ui-bar"><i style="width:55%"></i></div><div class="ui-bar"><i style="width:45%"></i></div><div class="ui-bar"><i style="width:75%"></i></div></div>
  </div>
  <div class="abs ui" style="left:303px;top:197px;width:235px;height:143px">
    <div class="ui-rail"></div>
    <div class="abs ui-title" style="left:20px;top:8px">Wave 1</div>
    <div class="abs" style="left:20px;top:22px;font-size:5px;color:var(--muted)">Raw Results Participants</div>
    <div class="abs" style="left:20px;top:34px;width:205px;height:6px;background:var(--navy)"></div>
    <div class="abs" style="left:20px;top:42px;width:205px"><div class="ui-row"></div><div class="ui-row"></div><div class="ui-row"></div><div class="ui-row"></div><div class="ui-row"></div><div class="ui-row"></div><div class="ui-row"></div><div class="ui-row"></div><div class="ui-row"></div><div class="ui-row"></div><div class="ui-row"></div><div class="ui-row"></div><div class="ui-row"></div><div class="ui-row"></div><div class="ui-row"></div><div class="ui-row"></div></div>
  </div>

  <div class="abs back-photo" role="img" aria-label="Dim photo of people working at laptops around a desk"></div>

  <p class="abs iterative">BRISKing members is an iterative process. Connect with members months before their renewal so you can address any issues and take the action required to retain at-risk members. And getting BRISK up and running only takes a few hours of effort. Your time is spent interacting with your members, no administering the platform.</p>

  <h2 class="abs section-title clients-title">OUR CLIENTS</h2>
  <div class="abs clients">
    <span>Lumera</span><span>Veritune</span><span>Oakmere</span><span>Careplan Union</span><span>Ridgeway Partners</span><span>Orvo</span><span>Bramble</span><span>Quillon</span>
    <span>Halberd Health</span><span>Northvale Health</span><span>Cedarhurst Care</span><span>Keystream</span><span>Warden Mutual</span><span>Corvane</span><span>Elmford Health</span>
    <span>Molara</span><span>Arcvo</span><span>Genwise</span><span>Prairie State</span>
  </div>

  <div class="abs contact">
    <h2>CONTACT INFO</h2>
    <p><span><b>Dale Hutton</b><br>CEO / Founder</span><svg width="12" height="12" viewBox="0 0 12 12"><circle cx="6" cy="3.5" r="2.6" fill="#fff"/><path d="M1 12c0-4 2.3-5.5 5-5.5s5 1.5 5 5.5z" fill="#fff"/></svg></p>
    <p>555-304-8216<svg width="12" height="12" viewBox="0 0 12 12"><path d="M2 1l2.5 0 1 3-1.5 1c.7 1.4 1.6 2.3 3 3l1-1.5 3 1V10c0 .6-.5 1-1 1C5 11 1 7 1 2c0-.5.4-1 1-1z" fill="#fff"/></svg></p>
    <p>dhutton@fernwick.example<svg width="12" height="12" viewBox="0 0 12 12"><rect x="0.5" y="2" width="11" height="8" fill="#fff"/><path d="M1 2.5l5 4 5-4" fill="none" stroke="var(--blue)" stroke-width="1"/></svg></p>
    <p>www.briskvlt.example<svg width="12" height="12" viewBox="0 0 12 12"><circle cx="6" cy="6" r="5" fill="none" stroke="#fff"/><path d="M1 6h10M6 1c-2.5 3-2.5 7 0 10M6 1c2.5 3 2.5 7 0 10" fill="none" stroke="#fff" stroke-width=".8"/></svg></p>
  </div>
  <div class="abs back-brand"><span class="sq"></span>BRISK</div>
</section>

</body>
</html>
```